Business Card for Toffee Parlour

I have a logo for my candy buffet business, and need a business card designed using that logo. Toffee Parlour designs and builds beautiful and delicious candy and dessert tables for all kinds of events. The card should be simple, modern, graphic, colorful, and use the Toffee Parlour Logo.

Target Market(s)

The target market is people hosting major parties and events. This includes brides getting married, parents hosting birthday parties/Sweet Sixteen/Bar Mitzvah/quinceanera parties, and companies hosting corporate events.

Industry/Entity Type

Business

Requirements
Must have
• The business card must have the logo, with or without the tag line.

The following information must be on the card:

Renata Hollis
CEO & Candy Stylist
415.372.6091
renata@toffeeparlourco.example
Nice to have
• I like the idea of having multiple colors of the same design so that several people receiving cards will each receive a different color. Perhaps 3-5 colors or variations on a basic card design.

```html
<!DOCTYPE html>
<html lang="en">
<head>
<meta charset="utf-8">
<title>Toffee Parlour — Business Cards</title>
<link rel="stylesheet" href="https://fonts.googleapis.com/css2?family=Jost:wght@300;400;600&display=swap">
<style>
  :root {
    --ink: #111111;
    --paper: #ffffff;
    --grape: #6560a8;
    --tangerine: #f9a541;
    --ocean: #2596d1;
    --berry: #e8097f;
    --lemon: #f2e93b;
    --mint: #21a04b;
    --sky: #35b8ea;
    --blush: #f07ab0;
    --rose: #ee8fc0;
    --tag: rgba(255,255,255,0.85);
  }
  html, body {
    margin: 0;
    padding: 0;
    width: 957px;
    height: 1200px;
    overflow: hidden;
    background: var(--paper);
    font-family: "Jost", "Century Gothic", sans-serif;
  }
  .sheet {
    position: relative;
    width: 957px;
    height: 1200px;
  }
  .card {
    position: absolute;
    width: 362px;
    height: 230px;
    box-sizing: border-box;
  }
  .card--front {
    left: 82px;
    border: 1px solid var(--ink);
    background: var(--paper);
    display: flex;
    align-items: center;
    justify-content: center;
  }
  .card--back { left: 467px; }
  .row-1 { top: 91px; }
  .row-2 { top: 334px; }
  .row-3 { top: 583px; }
  .row-4 { top: 825px; }

  .wordmark {
    margin: 0;
    margin-top: 22px;
    font-weight: 400;
    font-size: 42px;
    letter-spacing: -0.5px;
    color: var(--ink);
    line-height: 1;
  }

  .back--grape { background: var(--grape); }
  .back--tangerine { background: var(--tangerine); }
  .back--ocean { background: var(--ocean); }
  .back--berry { background: var(--berry); border: 1px solid var(--ink); }

  .tagline {
    position: absolute;
    top: 15px;
    left: 27px;
    right: 40px;
    display: flex;
    align-items: center;
    gap: 7px;
    font-size: 9.5px;
    font-weight: 300;
    color: var(--tag);
    white-space: nowrap;
  }
  .tagline::before,
  .tagline::after {
    content: "";
    flex: 1;
    height: 1px;
    background: var(--tag);
    opacity: 0.7;
  }

  .contact {
    position: absolute;
    left: 17px;
    top: 131px;
    margin: 0;
    font-size: 14px;
    font-weight: 300;
    line-height: 18px;
    font-style: normal;
  }
  .contact span { display: block; }
  .contact .surname { font-weight: 600; }

  .name { color: var(--lemon); }
  .phone { color: var(--mint); }

  .back--grape .role { color: var(--sky); }
  .back--grape .email { color: var(--blush); }
  .back--tangerine .role { color: var(--ocean); }
  .back--tangerine .email { color: var(--berry); }
  .back--ocean .role { color: var(--berry); }
  .back--ocean .email { color: var(--grape); }
  .back--berry .role { color: var(--sky); }
  .back--berry .email { color: var(--rose); }
</style>
</head>
<body>
<main class="sheet">

  <section class="card card--front row-1"><p class="wordmark">toffeeparlour</p></section>
  <section class="card card--back back--grape row-1">
    <p class="tagline">the best part of the party</p>
    <address class="contact">
      <span class="name">renata <b class="surname">hollis</b></span>
      <span class="role">ceo &amp; candy stylist</span>
      <span class="phone">415 372 6091</span>
      <span class="email">renata@toffeeparlourco.example</span>
    </address>
  </section>

  <section class="card card--front row-2"><p class="wordmark">toffeeparlour</p></section>
  <section class="card card--back back--tangerine row-2">
    <p class="tagline">the best part of the party</p>
    <address class="contact">
      <span class="name">renata <b class="surname">hollis</b></span>
      <span class="role">ceo &amp; candy stylist</span>
      <span class="phone">415 372 6091</span>
      <span class="email">renata@toffeeparlourco.example</span>
    </address>
  </section>

  <section class="card card--front row-3"><p class="wordmark">toffeeparlour</p></section>
  <section class="card card--back back--ocean row-3">
    <p class="tagline">the best part of the party</p>
    <address class="contact">
      <span class="name">renata <b class="surname">hollis</b></span>
      <span class="role">ceo &amp; candy stylist</span>
      <span class="phone">415 372 6091</span>
      <span class="email">renata@toffeeparlourco.example</span>
    </address>
  </section>

  <section class="card card--front row-4"><p class="wordmark">toffeeparlour</p></section>
  <section class="card card--back back--berry row-4">
    <p class="tagline">the best part of the party</p>
    <address class="contact">
      <span class="name">renata <b class="surname">hollis</b></span>
      <span class="role">ceo &amp; candy stylist</span>
      <span class="phone">415 372 6091</span>
      <span class="email">renata@toffeeparlourco.example</span>
    </address>
  </section>

</main>
</body>
</html>
```